Full Page print dental ad

Looking for a modern dental ad to promote our office and an Clarovent special $500 off and also show our Quelo techology.

website is harbordentalnorthwest.com
address is 24416 52nd ave NE Lakeview, Wa 98113
Phone is 206-555-0148

attached an ad that this will be replaceing, but we do not like it. but it has information that might be helpful.

looks for something a more modern and less busy

```html
<!DOCTYPE html>
<html lang="en">
<head>
<meta charset="utf-8">
<title>Northshore Dental – Your Local Family Dentist</title>
<link rel="stylesheet" href="https://fonts.googleapis.com/css2?family=Montserrat:wght@400;500;600;700;800&family=Open+Sans:wght@400;600&display=swap">
<style>
  :root{
    --navy:#2d3e50;
    --navy-dark:#233140;
    --green:#7cc242;
    --grey:#eef0f2;
    --text:#3a4654;
    --white:#ffffff;
  }
  *{box-sizing:border-box;margin:0;padding:0}
  html,body{width:861px;height:1200px;overflow:hidden;background:#f4f4f4}
  body{font-family:"Open Sans",Arial,sans-serif;color:var(--text)}
  .ad{position:relative;width:861px;height:1200px;background:var(--white);overflow:hidden}

  .header{position:absolute;left:0;top:0;width:861px;height:118px;display:flex}
  .brand{flex:1;display:flex;align-items:center;gap:14px;padding-left:40px}
  .brand-dot{width:40px;height:40px;border-radius:50%;background:var(--navy);flex:none}
  .brand-name{font-family:"Montserrat",sans-serif;font-weight:700;font-size:26px;color:var(--navy);line-height:1;white-space:nowrap}
  .benefits{width:420px;background:var(--navy);color:var(--white);display:flex;align-items:center;padding:0 34px;
    font-family:"Montserrat",sans-serif;font-weight:600;font-size:19px;line-height:1.35}
  .benefits strong{color:var(--green);font-weight:700}

  .hero{position:absolute;left:0;top:118px;width:861px;height:404px;
    background:linear-gradient(120deg,#dfe6ec 0%,#c9d3db 40%,#b7c2cc 100%)}
  .partner-badges{position:absolute;right:40px;top:22px;width:200px;height:96px;background:var(--white);
    border-radius:4px;padding:14px;display:flex;flex-direction:column;gap:12px;box-shadow:0 2px 8px rgba(0,0,0,.12)}
  .partner-badges span{display:block;height:28px;border-radius:3px;background:#cfd8df}
  .partner-badges span:last-child{background:#9fb7c7;width:70%}

  .headline{position:absolute;left:0;top:522px;width:861px;height:76px;background:var(--green);
    display:flex;align-items:center;justify-content:center;
    font-family:"Montserrat",sans-serif;font-weight:800;font-size:38px;color:var(--white);letter-spacing:.5px}
  .subline{position:absolute;left:0;top:598px;width:861px;height:40px;background:var(--navy);
    display:flex;align-items:center;justify-content:center;
    font-family:"Montserrat",sans-serif;font-weight:600;font-size:20px;color:var(--white)}

  .services{position:absolute;left:0;top:638px;width:400px;height:300px;background:var(--grey);padding:28px 30px 0 40px}
  .services li{list-style:none;display:flex;align-items:center;gap:10px;font-size:14px;font-weight:600;color:var(--navy);margin-bottom:12px}
  .services svg{flex:none}

  .intro{position:absolute;left:400px;top:638px;width:461px;height:300px;padding:26px 36px 0 36px}
  .intro p{font-size:13.5px;line-height:1.5;color:var(--text)}
  .team-photo{margin-top:16px;width:270px;height:150px;border-radius:2px;
    background:linear-gradient(135deg,#8aa0b4,#5e7489)}

  .online{position:absolute;left:0;top:938px;width:400px;height:180px;padding:22px 30px 0 40px}
  .online-title{display:inline-block;background:var(--green);color:var(--white);font-family:"Montserrat",sans-serif;
    font-weight:700;font-size:14px;padding:7px 14px;border-radius:3px;text-transform:uppercase}
  .online ul{margin-top:14px}
  .online li{list-style:none;display:flex;align-items:center;gap:10px;font-size:14px;color:var(--navy);margin-bottom:10px}
  .online li i{width:22px;height:22px;background:var(--navy);border-radius:3px;display:block;flex:none}

  .offer{position:absolute;left:400px;top:938px;width:461px;height:180px;padding:20px 30px;text-align:center;
    border-left:4px solid var(--green)}
  .offer-free{font-family:"Montserrat",sans-serif;font-weight:800;font-size:64px;color:var(--navy);line-height:1}
  .offer-what{font-family:"Montserrat",sans-serif;font-weight:700;font-size:18px;color:var(--navy);margin-top:6px;text-transform:uppercase}
  .offer-with{display:inline-block;margin-top:12px;background:var(--green);color:var(--white);font-family:"Montserrat",sans-serif;
    font-weight:600;font-size:13px;padding:6px 14px;border-radius:3px;text-transform:uppercase}

  .footer{position:absolute;left:0;top:1118px;width:861px;height:82px;background:var(--navy-dark);color:var(--white);
    display:flex;align-items:center;justify-content:space-between;padding:0 40px;font-size:14px}
  .footer-item{display:flex;align-items:center;gap:9px;white-space:nowrap}
</style>
</head>
<body>
<div class="ad">

  <header class="header">
    <div class="brand">
      <span class="brand-dot"></span>
      <span class="brand-name">Northshore Dental</span>
    </div>
    <div class="benefits">
      <p>Don't Forget To Use Up Your 2021 Dental Benefits <strong>Call Now!</strong></p>
    </div>
  </header>

  <section class="hero" role="img" aria-label="Photo of a smiling mother and daughter in a bright dental office">
    <div class="partner-badges" aria-hidden="true"><span></span><span></span></div>
  </section>

  <h1 class="headline">YOUR LOCAL FAMILY DENTIST</h1>
  <p class="subline">Now Accepting New Patients!</p>

  <ul class="services">
    <li><svg width="16" height="16" viewBox="0 0 16 16"><circle cx="8" cy="8" r="8" fill="#7cc242"/><path d="M4.5 8.2l2.3 2.3 4.7-4.8" fill="none" stroke="#fff" stroke-width="2"/></svg>Family, Cosmetic &amp; Implant Dentistry</li>
    <li><svg width="16" height="16" viewBox="0 0 16 16"><circle cx="8" cy="8" r="8" fill="#7cc242"/><path d="M4.5 8.2l2.3 2.3 4.7-4.8" fill="none" stroke="#fff" stroke-width="2"/></svg>Most Insurances Accepted</li>
    <li><svg width="16" height="16" viewBox="0 0 16 16"><circle cx="8" cy="8" r="8" fill="#7cc242"/><path d="M4.5 8.2l2.3 2.3 4.7-4.8" fill="none" stroke="#fff" stroke-width="2"/></svg>Clarovent Clear Aligners – $500 Off</li>
    <li><svg width="16" height="16" viewBox="0 0 16 16"><circle cx="8" cy="8" r="8" fill="#7cc242"/><path d="M4.5 8.2l2.3 2.3 4.7-4.8" fill="none" stroke="#fff" stroke-width="2"/></svg>Quelo Digital 3D Scanning</li>
    <li><svg width="16" height="16" viewBox="0 0 16 16"><circle cx="8" cy="8" r="8" fill="#7cc242"/><path d="M4.5 8.2l2.3 2.3 4.7-4.8" fill="none" stroke="#fff" stroke-width="2"/></svg>Same Day Crowns</li>
    <li><svg width="16" height="16" viewBox="0 0 16 16"><circle cx="8" cy="8" r="8" fill="#7cc242"/><path d="M4.5 8.2l2.3 2.3 4.7-4.8" fill="none" stroke="#fff" stroke-width="2"/></svg>Leading Edge Dental Technology</li>
    <li><svg width="16" height="16" viewBox="0 0 16 16"><circle cx="8" cy="8" r="8" fill="#7cc242"/><path d="M4.5 8.2l2.3 2.3 4.7-4.8" fill="none" stroke="#fff" stroke-width="2"/></svg>Early Mornings &amp; Evenings Available</li>
    <li><svg width="16" height="16" viewBox="0 0 16 16"><circle cx="8" cy="8" r="8" fill="#7cc242"/><path d="M4.5 8.2l2.3 2.3 4.7-4.8" fill="none" stroke="#fff" stroke-width="2"/></svg>Gentle Care For The Whole Family</li>
  </ul>

  <section class="intro">
    <p>For nearly two decades, our caring team has helped local families keep healthy, confident smiles. We welcome new patients of every age and look forward to meeting you.</p>
    <div class="team-photo" role="img" aria-label="Portrait of the two dentists of the practice"></div>
  </section>

  <section class="online">
    <span class="online-title">Find Us Online</span>
    <ul>
      <li><i></i>Linkup/northshoredental</li>
      <li><i></i>Reviews on Searchly</li>
      <li><i></i>harbordentalnorthwest.com</li>
    </ul>
  </section>

  <section class="offer">
    <div class="offer-free">FREE</div>
    <div class="offer-what">Teeth Whitening for New Patients</div>
    <span class="offer-with">With New Patient Exam &amp; Cleaning</span>
  </section>

  <footer class="footer">
    <span class="footer-item">
      <svg width="14" height="18" viewBox="0 0 14 18"><path d="M7 0a7 7 0 0 0-7 7c0 5 7 11 7 11s7-6 7-11a7 7 0 0 0-7-7z" fill="#7cc242"/><circle cx="7" cy="7" r="2.6" fill="#233140"/></svg>
      24416 52nd ave NE, Lakeview, WA 98113
    </span>
    <span class="footer-item">
      <svg width="16" height="16" viewBox="0 0 24 24"><path d="M6.6 10.8a15.1 15.1 0 0 0 6.6 6.6l2.2-2.2c.3-.3.7-.4 1-.2 1.1.4 2.3.6 3.6.6.6 0 1 .4 1 1V20c0 .6-.4 1-1 1A17 17 0 0 1 3 4c0-.6.4-1 1-1h3.5c.6 0 1 .4 1 1 0 1.3.2 2.5.6 3.6.1.3 0 .7-.2 1z" fill="#7cc242"/></svg>
      206-555-0148
    </span>
    <span class="footer-item">harbordentalnorthwest.com</span>
  </footer>

</div>
</body>
</html>
```